Brennick & Vale, LLC
Law firm stationary and business cards
Brennick & Vale, LLC -
Creative Brief
Professional
Miles R. Dorsey
2875 Oakridge Avenue, Suite 410 Kansas City, Missouri 64187
miles@brennickvale-law.example
www.brennickvale-law.example

```html
<!DOCTYPE html>
<html lang="en">
<head>
<meta charset="utf-8">
<title>Brennick &amp; Vale, LLC — Business Card</title>
<link href="https://fonts.googleapis.com/css2?family=Cinzel:wght@500&family=Tinos:wght@400;700&display=swap" rel="stylesheet">
<style>
  :root {
    --backdrop: #2e2f31;
    --card: #ffffff;
    --card-shade: #eef0f3;
    --brand-blue: #1d4f9e;
    --brand-blue-dark: #163f80;
    --ink: #2f2f33;
    --muted: #5a5a60;
    --pale-blue: #c9d4ea;
    --pale-grey: #e1e3e7;
  }
  * { margin: 0; padding: 0; box-sizing: border-box; }
  html, body { width: 1200px; height: 953px; overflow: hidden; }
  body {
    background: var(--backdrop);
    position: relative;
    font-family: "Tinos", "Times New Roman", serif;
    color: var(--ink);
  }
  .card {
    position: absolute;
    border-radius: 26px;
    overflow: hidden;
    background: linear-gradient(180deg, var(--card) 0%, var(--card) 60%, var(--card-shade) 100%);
  }
  .card--front { left: 70px; top: 75px; width: 798px; height: 381px; }
  .card--back  { left: 391px; top: 507px; width: 745px; height: 379px; }

  .rule-top {
    position: absolute; left: 0; right: 0; top: 22px; height: 3px;
    background: var(--brand-blue);
  }
  .name-band {
    position: absolute; left: 0; right: 0; top: 39px; height: 48px;
    background: linear-gradient(180deg, var(--brand-blue) 0%, var(--brand-blue-dark) 100%);
  }
  .person-name {
    position: absolute; right: 34px; top: 48px;
    font-weight: 700; font-size: 28px; line-height: 30px; color: #fff;
  }

  .firm-mark { position: absolute; }
  .firm-mark .mark-square {
    position: absolute; left: 0; top: 0; width: 46px; height: 46px;
    background: var(--brand-blue);
  }
  .firm-name {
    position: absolute; white-space: nowrap;
    font-family: "Cinzel", "Times New Roman", serif; font-weight: 500;
    color: var(--ink); letter-spacing: 0.5px;
  }
  .firm-rule { position: absolute; height: 1.5px; background: var(--ink); }
  .firm-tagline {
    position: absolute; white-space: nowrap;
    font-family: "Cinzel", "Times New Roman", serif; font-weight: 500;
    color: var(--ink); letter-spacing: 1px;
  }

  .card--front .firm-mark { left: 46px; top: 150px; width: 560px; height: 80px; }
  .card--front .firm-name { left: 76px; top: 8px; font-size: 29px; }
  .card--front .firm-rule { left: 76px; top: 48px; width: 368px; }
  .card--front .firm-tagline { left: 268px; top: 52px; font-size: 14px; }

  .contact {
    position: absolute; left: 124px; top: 230px;
    font-size: 15px; line-height: 23px; color: var(--ink);
    list-style: none;
  }
  .contact .label { color: var(--brand-blue); font-weight: 700; }

  .deco-square { position: absolute; }
  .card--front .deco-square {
    right: 36px; bottom: 22px; width: 132px; height: 132px;
    background: var(--pale-blue); opacity: 0.55; border-radius: 20px;
  }
  .card--back .deco-square {
    left: 130px; top: -40px; width: 250px; height: 300px;
    background: var(--pale-blue); opacity: 0.6; border-radius: 40px;
  }

  .card--back .firm-mark { left: 291px; top: 272px; width: 420px; height: 80px; }
  .card--back .firm-name { left: 0; top: 8px; font-size: 29px; }
  .card--back .firm-rule { left: 0; top: 46px; width: 368px; }
  .card--back .firm-tagline { left: 192px; top: 50px; font-size: 14px; }
</style>
</head>
<body>

  <section class="card card--front" aria-label="Business card front">
    <div class="rule-top"></div>
    <div class="name-band"></div>
    <h1 class="person-name">Miles R. Dorsey</h1>

    <div class="firm-mark">
      <span class="mark-square"></span>
      <span class="firm-name">BRENNICK &amp; VALE, LLC</span>
      <span class="firm-rule"></span>
      <span class="firm-tagline">TRIAL ATTORNEYS</span>
    </div>

    <ul class="contact">
      <li>2875 Oakridge Avenue, Suite 410</li>
      <li>Kansas City, Missouri 64187</li>
      <li><span class="label">P</span> : (816) 555-0142</li>
      <li><span class="label">F</span> : (816) 555-0147</li>
      <li><span class="label">E</span> : miles@brennickvale-law.example</li>
      <li><span class="label">W</span> : www.brennickvale-law.example</li>
    </ul>

    <div class="deco-square" aria-hidden="true"></div>
  </section>

  <section class="card card--back" aria-label="Business card back">
    <div class="deco-square" aria-hidden="true"></div>
    <div class="firm-mark">
      <span class="firm-name">BRENNICK &amp; VALE, LLC</span>
      <span class="firm-rule"></span>
      <span class="firm-tagline">TRIAL ATTORNEYS</span>
    </div>
  </section>

</body>
</html>
```